REAL ESTATE MAILBOX DROP FLYER

I am looking for two flyer designs. One for DL and one for A4 size. My company is a boutique real estate agency that offers a full/high quality service at a very low commission rate.

Key Phrases to be included

A4 Design should have a space for some text and a table in the center (outline below)

Target Market(s)

Home Owners

Industry/Entity Type

Real Estate Agent

Colors
0455a3

Requirements
Must have
• Eye Catching
• Bold
• high end feel
• Color pallette should match the logo
• The feel of the brochures must convey a trustworthy, high end service.
• Must be eye catching and easy to read
• Editable file formats must be supplied

```html
<!DOCTYPE html>
<html lang="en">
<head>
<meta charset="utf-8">
<title>Lowline Property – Flyers</title>
<link href="https://fonts.googleapis.com/css2?family=Montserrat:wght@300;400;500;600;700;800;900&family=Tinos:wght@400;700&display=swap" rel="stylesheet">
<style>
:root{
  --navy:#0b2240;
  --red:#e3151c;
  --copper:#b57248;
  --white:#ffffff;
  --ink:#222a33;
  --rule:#8a8f96;
  --board:#5f5f5f;
}
*{margin:0;padding:0;box-sizing:border-box}
html,body{width:1200px;height:800px;overflow:hidden;background:var(--board)}
body{position:relative;font-family:'Montserrat',sans-serif;color:var(--ink)}
.flyer{position:absolute;background:var(--white);overflow:hidden}
.a4{left:54px;top:164px;width:389px;height:548px}
.dl{left:464px;top:260px;width:712px;height:356px}
.abs{position:absolute}
svg.art{position:absolute;left:0;top:0}
.brand{position:absolute;color:var(--white);font-weight:600;line-height:.95;text-align:center;letter-spacing:.5px}

/* A4 */
.a4 .tagline{left:12px;top:16px;color:var(--white);font-weight:800;font-size:12.5px;line-height:1.25}
.a4 .tagline .big{font-size:16px}
.a4 .tagline .pct{position:absolute;left:56px;top:-6px;color:var(--copper);font-size:34px;font-weight:900;letter-spacing:-1px}
.a4 .brand{right:10px;top:34px;font-size:15px}
.a4 .brand span{display:block;font-size:18px}
.headline{font-weight:300;white-space:nowrap}
.headline .chip{background:var(--navy);color:var(--white);border-radius:4px;padding:0 3px}
.headline b{font-weight:700}
.a4 .headline{left:0;right:0;top:302px;text-align:center;font-size:15.5px}
.a4 .copy{left:22px;right:20px;top:327px;font-size:6.8px;line-height:1.35}
.a4 .copy p{margin-bottom:8px}
.data{position:absolute;left:21px;top:396px;width:342px;border-collapse:collapse;font-family:'Tinos',serif;font-size:5px;color:#333}
.data thead th{background:#e6e6e6;font-weight:400;padding:2px 2px;text-align:center}
.data tbody td{padding:1.3px 2px;text-align:center}
.data td.var{text-align:left}
.data tr.group td{border-top:.5px solid var(--rule)}
.a4 .contact{left:20px;top:494px;font-size:11px;font-weight:300;line-height:1.25;white-space:nowrap}
.a4 .contact .phone{font-family:'Tinos',serif;font-size:18px;font-weight:700;color:var(--navy)}
.a4 .contact .free{background:var(--navy);color:var(--white);padding:0 3px;font-size:10px;font-weight:400}
.a4 .contact .free b{font-weight:600}
.a4 .foot{left:154px;top:494px;width:235px;height:47px;background:var(--navy);clip-path:polygon(10px 0,100% 0,100% 100%,0 100%);color:var(--white);text-align:center;padding-top:6px}
.a4 .foot .slogan{font-size:11.5px;font-weight:300}
.a4 .foot .slogan b{font-weight:600}
.a4 .foot .mail{font-size:8px;font-weight:300;line-height:1.35;margin-top:2px}

/* DL */
.dl .brand{left:12px;top:30px;font-size:12px}
.dl .brand span{display:block;font-size:15px}
.dl .offer{left:416px;top:20px;color:var(--red);font-weight:900;line-height:1}
.dl .offer .l1{font-size:19px}
.dl .offer .l2{font-size:19px;margin-top:7px}
.dl .offer .l3{font-size:33px;margin-top:4px}
.dl .offer .pct{position:absolute;left:128px;top:-4px;font-size:58px;letter-spacing:-2px}
.dl .save{left:416px;top:115px;color:var(--white);font-size:24px;font-weight:300;line-height:1.25}
.dl .save .chip{background:var(--white);color:var(--navy);border-radius:5px;padding:0 4px}
.dl .save b{font-weight:700}
.dl .contact{left:16px;top:302px;font-size:15.5px;font-weight:300;letter-spacing:-.2px;white-space:nowrap}
.dl .free{left:16px;top:327px;background:var(--navy);color:var(--white);font-size:13.5px;font-weight:300;padding:1px 4px;white-space:nowrap}
.dl .free b{font-weight:600}
.dl .phonebox{left:196px;top:298px;width:172px;height:58px;background:var(--navy);color:var(--white);font-family:'Tinos',serif;font-weight:700;font-size:27px;display:flex;align-items:center;justify-content:center}
.dl .footbox{left:370px;top:298px;width:342px;height:58px;background:var(--navy);color:var(--white);text-align:center;padding-top:9px}
.dl .footbox .slogan{font-size:21px;font-weight:300}
.dl .footbox .slogan b{font-weight:600}
.dl .footbox .mail{font-size:8.5px;font-weight:300;margin-top:2px}
.mail b{font-weight:600}
</style>
</head>
<body>

<section class="flyer a4">
  <svg class="art" width="389" height="290" viewBox="0 0 389 290">
    <defs>
      <linearGradient id="roomA4" x1="0" y1="0" x2="0" y2="1">
        <stop offset="0" stop-color="#e9e7e2"/><stop offset=".6" stop-color="#c9c3ba"/><stop offset="1" stop-color="#8f8477"/>
      </linearGradient>
      <linearGradient id="bedA4" x1="0" y1="0" x2="1" y2="1">
        <stop offset="0" stop-color="#e6e4e0"/><stop offset="1" stop-color="#6e6a66"/>
      </linearGradient>
      <linearGradient id="kitA4" x1="0" y1="0" x2="1" y2="1">
        <stop offset="0" stop-color="#f1efe9"/><stop offset="1" stop-color="#a68a63"/>
      </linearGradient>
    </defs>
    <rect width="389" height="148" fill="var(--navy)"/>
    <polygon points="195,21 368,136 368,256 18,256 18,136" fill="var(--white)"/>
    <g role="img" aria-label="Living room interior with sofas and dining table">
      <polygon points="195,30 361,138 361,148 389,148 389,256 0,256 0,148 25,148 25,138" fill="url(#roomA4)"/>
    </g>
    <rect x="27" y="203" width="160" height="80" fill="var(--white)"/>
    <rect x="203" y="203" width="160" height="80" fill="var(--white)"/>
    <rect role="img" aria-label="Bedroom interior" x="29" y="206" width="156" height="75" fill="url(#bedA4)"/>
    <rect role="img" aria-label="Open plan kitchen and lounge" x="205" y="206" width="156" height="75" fill="url(#kitA4)"/>
  </svg>

  <div class="abs tagline">Top Tier<br>Service,<br><span class="big">Commission</span><span class="pct">1%</span></div>
  <div class="brand">LOWLINE<span>PROPERTY</span></div>

  <div class="abs headline"><span class="chip">Save <b>THOUSANDS</b></span> On <b>COMMISSIONS!</b></div>

  <div class="abs copy">
    <p>Lorem ipsum dolor sit amet, consectetur adipiscing elit, sed do eiusmod tempor incididunt ut labore et dolore magna aliqua. Ut enim ad minim veniam, quis nostrud exercitation ullamco laboris nisi ut aliquip ex ea commodo consequat.</p>
    <p>Duis aute irure dolor in reprehenderit in voluptate velit esse cillum dolore eu fugiat nulla pariatur. Excepteur sint occaecat cupidatat non proident, sunt in culpa qui officia deserunt mollit anim id est</p>
  </div>

  <table class="data">
    <thead>
      <tr><th rowspan="3">Variable</th><th></th><th>Certified farms</th><th>Non-certified farms</th><th>Chi-square</th></tr>
      <tr><th></th><th>(n=32)</th><th>(n=52)</th><th>(p)</th></tr>
      <tr><th></th><th>Freq. (%)</th><th>Freq. (%)</th><th></th></tr>
    </thead>
    <tbody>
      <tr class="group"><td class="var" rowspan="2">Relationship</td><td>No</td><td>75</td><td>96</td><td rowspan="2">0.0105</td></tr>
      <tr><td>Yes</td><td>25</td><td>4</td></tr>
      <tr class="group"><td class="var" rowspan="2">Agricultural newsletter</td><td>No</td><td>47</td><td>81</td><td rowspan="2">0.0012</td></tr>
      <tr><td>Yes</td><td>53</td><td>19</td></tr>
      <tr class="group"><td class="var" rowspan="2">Certification experience</td><td>No</td><td>63</td><td>94</td><td rowspan="2">0.0007</td></tr>
      <tr><td>Yes</td><td>38</td><td>6</td></tr>
    </tbody>
  </table>

  <div class="abs contact">Contact Marcus today<br>on <span class="phone">0400 172 386</span><br><span class="free">for a <b>FREE APPRAISAL!</b></span></div>
  <div class="abs foot">
    <div class="slogan">More <b>Money</b> in YOUR Pocket!</div>
    <div class="mail">marcus@<b>lowlineproperty</b>.com.au<br>www.<b>lowlineproperty</b>.com.au</div>
  </div>
</section>

<section class="flyer dl">
  <svg class="art" width="712" height="300" viewBox="0 0 712 300">
    <defs>
      <linearGradient id="roomDL" x1="0" y1="0" x2="0" y2="1">
        <stop offset="0" stop-color="#e9e7e2"/><stop offset=".6" stop-color="#c9c3ba"/><stop offset="1" stop-color="#8f8477"/>
      </linearGradient>
      <linearGradient id="bedDL" x1="0" y1="0" x2="1" y2="1">
        <stop offset="0" stop-color="#e6e4e0"/><stop offset="1" stop-color="#6e6a66"/>
      </linearGradient>
      <linearGradient id="kitDL" x1="0" y1="0" x2="1" y2="1">
        <stop offset="0" stop-color="#f1efe9"/><stop offset="1" stop-color="#a68a63"/>
      </linearGradient>
    </defs>
    <rect width="712" height="176" fill="var(--navy)"/>
    <polygon points="188,10 352,112 352,236 0,236 0,112 22,112" fill="var(--white)"/>
    <g role="img" aria-label="Living room interior with sofas and dining table">
      <polygon points="188,19 345,116 345,236 0,236 0,124 28,124 28,116" fill="url(#roomDL)"/>
    </g>
    <rect x="16" y="210" width="154" height="76" fill="var(--white)"/>
    <rect x="184" y="210" width="154" height="76" fill="var(--white)"/>
    <rect role="img" aria-label="Bedroom interior" x="19" y="212" width="148" height="72" fill="url(#bedDL)"/>
    <rect role="img" aria-label="Open plan kitchen and lounge" x="187" y="212" width="148" height="72" fill="url(#kitDL)"/>
  </svg>

  <div class="brand">LOWLINE<span>PROPERTY</span></div>

  <div class="abs offer">
    <div class="l1">Full Service</div>
    <div class="l2">Agency</div>
    <div class="l3">Commission</div>
    <span class="pct">1%</span>
  </div>
  <div class="abs save"><span class="chip">Save <b>THOUSANDS</b></span><br>On <b>COMMISSIONS!</b></div>

  <div class="abs contact">Contact Marcus today</div>
  <div class="abs free">for a <b>FREE APPRAISAL!</b></div>
  <div class="abs phonebox">0400 172 386</div>
  <div class="abs footbox">
    <div class="slogan">More <b>Money</b> in YOUR Pocket!</div>
    <div class="mail">marcus@<b>lowlineproperty</b>.com.au | www.<b>lowlineproperty</b>.com.au</div>
  </div>
</section>

</body>
</html>
```